KVTA Promo Flyer for Corporate Events

Need a 8 page company overview

Target Market(s)

Creditors and Service Providers

Industry/Entity Type

Credit Card

Font styles to use
Serif

Colors
0455a3
fbf289

Requirements
Must have
• Fantastic Material and Creative
Nice to have
• Creative and personal

```html
<!DOCTYPE html>
<html lang="en">
<head>
<meta charset="utf-8">
<title>KVTA Company Overview – Covers</title>
<link rel="stylesheet" href="https://fonts.googleapis.com/css2?family=Questrial&display=swap">
<style>
  :root {
    --backdrop: #5d6770;
    --navy: #0a3a5c;
    --mist: #d3d4d6;
    --paper: #ffffff;
    --sky-top: #dfe8f7;
    --ink: #3d4a57;
    --ink-soft: #6b7580;
    --rule: #c3c7cc;
  }
  * { margin: 0; padding: 0; box-sizing: border-box; }
  html, body { width: 1200px; height: 789px; overflow: hidden; }
  body {
    background: var(--backdrop);
    font-family: "Questrial", sans-serif;
    color: var(--ink);
    position: relative;
  }
  .spread {
    position: absolute;
    left: 180px; top: 97px;
    width: 840px; height: 594px;
    display: flex;
    box-shadow: 0 10px 30px rgba(0,0,0,.3);
  }
  .cover { position: relative; width: 420px; height: 594px; overflow: hidden; }

  /* back cover */
  .back-cover { background: var(--navy); }
  .back-cover .cover-shape { position: absolute; inset: 0; }
  .back-cover .identity {
    position: absolute; left: 0; right: 0; top: 430px;
    text-align: center;
  }
  .company-name {
    font-size: 21px; letter-spacing: 1.5px;
    color: var(--ink); text-transform: uppercase;
  }
  .company-tagline {
    font-size: 9px; letter-spacing: 1.5px; color: var(--ink-soft);
    margin-top: 3px;
  }
  .contact {
    margin-top: 22px; font-size: 10.5px; line-height: 1.7; color: var(--ink);
  }

  /* front cover */
  .front-cover {
    background: linear-gradient(180deg, var(--sky-top) 0%, var(--paper) 30%, var(--paper) 55%);
  }
  .front-cover .identity {
    position: absolute; left: 0; right: 0; top: 70px; text-align: center;
  }
  .headline {
    position: absolute; left: 50px; right: 50px; top: 185px;
    padding: 14px 0;
    border-top: 1px solid var(--rule);
    border-bottom: 1px solid var(--rule);
    text-align: center;
    font-size: 12.5px; line-height: 1.6; color: var(--ink);
  }
  .skyline-photo {
    position: absolute; left: 0; right: 0; bottom: 0; height: 300px;
    background:
      linear-gradient(180deg, rgba(255,255,255,1) 0%, rgba(232,238,248,0) 22%),
      linear-gradient(180deg, #e9eef8 0%, #c9d6ec 30%, #8aa0c4 52%, #5a7088 66%, #7c8a4a 78%, #b58a3a 88%, #4f6b32 100%);
  }
</style>
</head>
<body>
  <main class="spread">
    <section class="cover back-cover">
      <svg class="cover-shape" width="420" height="594" viewBox="0 0 420 594" aria-hidden="true">
        <path d="M0,594 L0,430 C70,330 250,295 420,292 L420,594 Z" fill="var(--mist)"/>
        <path d="M0,470 C40,370 230,312 420,292 C250,318 70,372 22,468 Z" fill="var(--paper)"/>
      </svg>
      <div class="identity">
        <p class="company-name">Kestrel Valley Trade Associates</p>
        <p class="company-tagline">Accounts Receivable Management</p>
        <div class="contact">
          <p>Your Receivables Management Partner</p>
          <p>4470 Harbor Ridge Avenue Suite 310 Lakemont, WA</p>
          <p>(800) 555-0142 &nbsp;|&nbsp; kvta.net</p>
        </div>
      </div>
    </section>

    <section class="cover front-cover">
      <div class="identity">
        <p class="company-name">Kestrel Valley Trade Associates</p>
        <p class="company-tagline">Accounts Receivable Management</p>
      </div>
      <p class="headline">Navigating The Uncharted Waters Ahead<br>With an Experienced Debt Collection Agency...</p>
      <div class="skyline-photo" role="img" aria-label="City skyline beneath a snow-capped mountain at sunrise, with autumn trees in the foreground"></div>
    </section>
  </main>
</body>
</html>
```